Corvella Group Tank Card. New Design

We need a new design for our Credit Card Tank. We want a modern design using our logo colors. Our Card measures are 8,5cmX5,5cm. You can upgrade our logo design too. We are looking for modern and cool design. Our card printers can print the card number and holder in white color then you can use the colors you want for the background.

Target Market(s)

Gas station customers

Industry/Entity Type

Credit Card

Font styles to use
Sans Serif

Colors
a54499
b768aa
d2a4cc
acd036
cadf82
9bcb3b

Requirements
Must have
• Cool Design

```html
<!DOCTYPE html>
<html lang="en">
<head>
<meta charset="utf-8">
<title>Corvella Group — Client Plus Tank Card</title>
<link href="https://fonts.googleapis.com/css2?family=Roboto:wght@400;700&family=Encode+Sans+Condensed:wght@400;500&family=Oswald:wght@600&display=swap" rel="stylesheet">
<style>
  :root{
    --lime:#9bcb3b;
    --lime-light:#acd036;
    --lime-deep:#86b51c;
    --olive:#5b7a08;
    --magenta:#cc0aa6;
    --gold-light:#f6dc86;
    --gold:#dcaa32;
    --gold-dark:#9a6c14;
    --ink:#111;
    --white:#fff;
    --stripe:#000;
  }
  *{box-sizing:border-box;margin:0;padding:0}
  html,body{width:1200px;height:1200px;overflow:hidden;background:var(--white)}
  body{position:relative;font-family:"Roboto",Arial,sans-serif}

  .card{
    position:absolute;overflow:hidden;border-radius:24px;
    background:
      linear-gradient(135deg,rgba(255,255,255,.10) 0%,rgba(0,0,0,0) 40%,rgba(0,0,0,.06) 100%),
      linear-gradient(160deg,var(--lime-light) 0%,var(--lime) 45%,var(--lime-deep) 100%);
  }
  .card--portrait{left:38px;top:137px;width:386px;height:597px}
  .card--back{left:539px;top:139px;width:597px;height:386px}
  .card--front{left:539px;top:589px;width:598px;height:386px}

  .art{position:absolute;inset:0;width:100%;height:100%}

  .brand{position:absolute;display:flex;align-items:center;gap:10px}
  .brand__dot{width:48px;height:48px;border-radius:50%;background:var(--magenta);border:3px solid var(--white);flex:none}
  .brand__name{color:var(--white);font-weight:700;font-size:34px;letter-spacing:1px;text-transform:uppercase;white-space:nowrap}

  .tier{position:absolute;color:var(--white);font-weight:400;white-space:nowrap;line-height:1}
  .tier__word{font-size:42px;letter-spacing:1px}
  .tier__level{font-size:56px;letter-spacing:1px}

  .card--portrait .brand{left:12px;top:215px}
  .card--portrait .tier{left:56px;top:280px}
  .card--front .brand{left:19px;top:130px}
  .card--front .tier{left:93px;top:188px}

  .back__title{position:absolute;right:22px;top:24px;font-family:"Oswald",sans-serif;font-weight:600;font-size:22px;letter-spacing:1.5px;color:var(--white);word-spacing:10px}
  .back__stripe{position:absolute;left:0;right:0;top:77px;height:72px;background:var(--stripe)}
  .back__terms{position:absolute;left:19px;top:172px;width:554px;font-family:"Encode Sans Condensed",sans-serif;font-size:16.4px;line-height:19.6px;color:var(--ink);text-align:justify}
  .back__company{position:absolute;right:22px;top:293px;font-family:"Encode Sans Condensed",sans-serif;font-size:14px;letter-spacing:.8px;color:var(--ink)}
  .back__phone{position:absolute;right:22px;top:314px;display:flex;align-items:center;gap:6px;font-family:"Encode Sans Condensed",sans-serif;font-size:25px;color:var(--ink)}
  .back__phone svg{width:20px;height:20px}
  .back__note{position:absolute;right:20px;top:349px;font-family:"Encode Sans Condensed",sans-serif;font-size:9px;color:var(--ink)}
  .card--back .brand{left:19px;top:334px;gap:5px}
  .card--back .brand__dot{width:24px;height:24px;border-width:2px}
  .card--back .brand__name{font-size:17px}
</style>
</head>
<body>

<!-- Portrait front -->
<section class="card card--portrait">
  <svg class="art" viewBox="0 0 386 597" aria-hidden="true">
    <defs>
      <linearGradient id="goldA" x1="0" y1="0" x2="1" y2="1">
        <stop offset="0" stop-color="var(--gold-light)"/>
        <stop offset=".55" stop-color="var(--gold)"/>
        <stop offset="1" stop-color="var(--gold-dark)"/>
      </linearGradient>
    </defs>
    <g role="img" aria-label="Golden page curl revealing flowing oil">
      <path d="M386,313 L386,597 L192,597 Q250,470 386,313 Z" fill="url(#goldA)"/>
    </g>
  </svg>
  <div class="brand"><span class="brand__dot"></span><span class="brand__name">Corvella Group</span></div>
  <div class="tier"><span class="tier__word">CLIENT</span> <span class="tier__level">PLUS</span></div>
</section>

<!-- Back -->
<section class="card card--back">
  <h2 class="back__title">GASOIL PROFESSIONAL</h2>
  <div class="back__stripe"></div>
  <p class="back__terms">Lorem ipsum dolor sit amet, ridens mollis abhorreant at sea. Sed quaestio imperdiet ex. In his consul option, persequeris appellantur nam ea, et usu duis sensibus. Qui an nonumy quaestio scripserit, eum summo aliquid eligendi in, quo no veri tamquam persequeris. Quo epicurei pericula quaerendum no, ea eos prompta commune. Vis elitr labore ex, vero cibo libris eu nec. Ullum vivendum consetetur te vis, ferri maiorum torquatos eos et.</p>
  <div class="back__company">NORVESSA FUSION S.L.</div>
  <div class="back__phone">
    <svg viewBox="0 0 20 20" aria-hidden="true"><rect width="20" height="20" rx="4" fill="var(--magenta)"/><path d="M6 4.5c.6 0 1.6 2.4 1.6 2.9s-1 1-.9 1.5c.3 1.2 2.2 3.1 3.4 3.4.5.1 1-.9 1.5-.9s2.9 1 2.9 1.6-.9 2.5-2.4 2.5C8.3 15.5 4.5 11.7 4.5 8.1 4.5 6.6 5.4 4.5 6 4.5z" fill="var(--white)"/></svg>
    <span>700 318 542</span>
  </div>
  <div class="back__note">Lorem ipsum dolor sit amet, ridens mollis abhorreant at sea.</div>
  <div class="brand"><span class="brand__dot"></span><span class="brand__name">Corvella Group</span></div>
</section>

<!-- Landscape front -->
<section class="card card--front">
  <svg class="art" viewBox="0 0 598 386" aria-hidden="true">
    <defs>
      <linearGradient id="goldB" x1="0" y1="0" x2="1" y2="1">
        <stop offset="0" stop-color="var(--gold-dark)"/>
        <stop offset=".45" stop-color="var(--gold-light)"/>
        <stop offset="1" stop-color="var(--gold)"/>
      </linearGradient>
    </defs>
    <g role="img" aria-label="Golden page curl revealing flowing oil">
      <path d="M315,0 L598,0 L598,191 Q425,195 315,0 Z" fill="url(#goldB)"/>
    </g>
    <path d="M413,0 L598,0 L598,87 Q500,62 413,0 Z" fill="var(--magenta)"/>
  </svg>
  <div class="brand"><span class="brand__dot"></span><span class="brand__name">Corvella Group</span></div>
  <div class="tier"><span class="tier__word">CLIENT</span> <span class="tier__level">PLUS</span></div>
</section>

</body>
</html>
```